Men’s hair skin and beard line

I own a men’s salon in Texas and are beginning to expand its market into the men’s retail line and already have it being manufactured out of the UK. It’s paraben free, vegan, sulphate free. I need a better brand look for the packaging. This script font is a bit hard to read. I want it masculine yet clean lines. All colors even gold or silver are welcomed. Bottle choices are silver canisters, white or black.

Target Market(s)

Men

Industry/Entity Type

Men’s hair skin and beard industry. Retail centers, high end barbers, and gyms

Font styles to use
Other font styles liked:
• Montserrat ,helvetica neue, or lato font

Colors
0054AA
0677BA
7BADD7
CADEEF
E8F1F8
0094D4
00A9DD
6FCCEA
C7EBF8
E9F6FB
00AB8E
00BBA5
67D7C9
C6EFE9
E9F9F6

Requirements
Must have
• Logo and name
Nice to have
• I’m open to all.
Should not have
• Not feminine

```html
<!DOCTYPE html>
<html lang="en">
<head>
<meta charset="utf-8">
<title>Vantor Grooming Labels</title>
<link href="https://fonts.googleapis.com/css2?family=Bebas+Neue&family=Montserrat:wght@700&family=Oswald:wght@300;400&display=swap" rel="stylesheet">
<style>
  :root {
    --page: #ffffff;
    --label: #1c1c1c;
    --gold: #b99d62;
    --gold-light: #d9c797;
    --gold-dark: #a98c52;
  }
  * { margin: 0; padding: 0; box-sizing: border-box; }
  html, body { width: 1200px; height: 900px; overflow: hidden; background: var(--page); }
  .canvas { position: relative; width: 1200px; height: 900px; }

  .label { position: absolute; background: var(--label); color: var(--gold); text-align: center; }
  .label--beard-oil { left: 260px; top: 350px; width: 282px; height: 461px; }
  .label--cleanser { left: 644px; top: 89px; width: 328px; height: 722px; }

  .brand {
    position: absolute; left: 0; right: 0;
    display: flex; align-items: center; justify-content: center; gap: 10px;
    font-family: "Montserrat", sans-serif; font-weight: 700;
    color: var(--gold); letter-spacing: 0.04em;
  }
  .brand__mark { width: 12px; height: 12px; background: var(--gold); }
  .label--beard-oil .brand { top: 96px; font-size: 30px; }
  .label--cleanser .brand { top: 96px; font-size: 34px; }

  .product-name {
    position: absolute; left: 0; right: 0;
    font-family: "Bebas Neue", sans-serif; line-height: 0.86;
    background: linear-gradient(90deg, var(--gold-dark), var(--gold-light) 50%, var(--gold-dark));
    -webkit-background-clip: text; background-clip: text; color: transparent;
  }
  .label--beard-oil .product-name { top: 243px; font-size: 66px; }
  .label--cleanser .product-name { top: 305px; font-size: 76px; }

  .product-variant {
    position: absolute; left: 0; right: 0;
    font-family: "Oswald", sans-serif; font-weight: 400; color: var(--gold);
  }
  .label--beard-oil .product-variant { top: 308px; font-size: 16px; letter-spacing: 0.42em; padding-left: 0.42em; }
  .label--cleanser .product-variant { top: 440px; font-size: 16px; letter-spacing: 0.18em; padding-left: 0.18em; }

  .rule { position: absolute; height: 2px; background: linear-gradient(90deg, var(--gold-dark), var(--gold-light), var(--gold-dark)); }
  .label--beard-oil .rule { left: 19px; right: 16px; }
  .label--cleanser .rule { left: 21px; right: 16px; }

  .volume {
    position: absolute; left: 0; right: 0; top: 410px;
    font-family: "Oswald", sans-serif; font-weight: 400; font-size: 17px; color: var(--gold-light);
  }
  .label--cleanser .volume { top: 671px; }

  .description {
    position: absolute; left: 40px; right: 35px; top: 590px;
    font-family: "Oswald", sans-serif; font-weight: 300; font-size: 11.5px; line-height: 19px;
    text-align: justify; color: var(--gold); text-transform: uppercase;
  }
</style>
</head>
<body>
<main class="canvas">
  <section class="label label--beard-oil">
    <div class="brand"><span class="brand__mark"></span>VANTOR</div>
    <h1 class="product-name">BEARD OIL</h1>
    <p class="product-variant">CEDARWOOD FRAGRANCE</p>
    <div class="rule" style="top:398px"></div>
    <p class="volume">30ML / 1.0FL.OZ</p>
    <div class="rule" style="top:444px"></div>
  </section>

  <section class="label label--cleanser">
    <div class="brand"><span class="brand__mark"></span>VANTOR</div>
    <h1 class="product-name">FACIAL<br>CLEANSER</h1>
    <p class="product-variant">POST WASH FACIAL CLEANSER</p>
    <div class="rule" style="top:573px"></div>
    <p class="description">Enriched with organic aloe vera that gently cleanses the surface oil and impurities from your skin, while having your face rehydrated and rejuvinated</p>
    <div class="rule" style="top:659px"></div>
    <p class="volume">100ML / 3.4FL.OZ</p>
    <div class="rule" style="top:705px"></div>
  </section>
</main>
</body>
</html>
```